Stationery Design Project

We need a stationery design for a new business consulting business based in New Zealand.
We have the logo and business cards designed and we're looking for letterhead, compliments slip and PowerPoint presentation format that aligns with our business cards.
Industry/Entity Type
Business
Requirements
Must have
- same colors and format as business cards

```html
<!DOCTYPE html>
<html lang="en">
<head>
<meta charset="utf-8">
<title>Kowhai Advisory – Letterhead</title>
<link rel="stylesheet" href="https://fonts.googleapis.com/css2?family=Questrial&display=swap">
<style>
  :root {
    --brand-green: #78b22b;
    --band-light: #f4f4f4;
    --band-dark: #dcdcdc;
    --side-grey: #9a9a9a;
    --text-grey: #7a7a7a;
    --paper: #ffffff;
  }
  html, body {
    margin: 0;
    padding: 0;
    overflow: hidden;
    background: var(--paper);
  }
  .letterhead {
    position: relative;
    width: 849px;
    height: 1200px;
    background: var(--paper);
    overflow: hidden;
    font-family: "Questrial", "Century Gothic", sans-serif;
  }
  .header-band {
    position: absolute;
    left: 0;
    top: 0;
    width: 849px;
    height: 263px;
    background: radial-gradient(ellipse 520px 260px at 300px 120px, var(--band-light) 0%, #e6e6e6 60%, var(--band-dark) 100%);
  }
  .accent-bar {
    position: absolute;
    left: 265px;
    top: 0;
    width: 584px;
    height: 19px;
    background: var(--brand-green);
  }
  .side-tab {
    position: absolute;
    left: 0;
    top: 150px;
    width: 20px;
    height: 210px;
    background: var(--side-grey);
  }
  .company-name {
    position: absolute;
    left: 140px;
    top: 100px;
    margin: 0;
    font-size: 42px;
    font-weight: 400;
    line-height: 1;
    color: var(--brand-green);
    letter-spacing: 0.2px;
  }
  .contact-block {
    position: absolute;
    left: 583px;
    top: 134px;
    margin: 0;
    padding: 0;
    list-style: none;
    font-size: 14.5px;
    color: var(--text-grey);
    line-height: 21.5px;
  }
  .contact-block li {
    display: flex;
    align-items: center;
    white-space: nowrap;
  }
  .contact-icon {
    width: 12px;
    height: 12px;
    margin-right: 9px;
    flex: none;
  }
  .contact-icon path, .contact-icon circle, .contact-icon rect {
    fill: none;
    stroke: var(--brand-green);
    stroke-width: 1.3;
  }
  .contact-icon .solid {
    fill: var(--brand-green);
    stroke: none;
  }
</style>
</head>
<body>
  <main class="letterhead">
    <div class="header-band"></div>
    <div class="accent-bar"></div>
    <div class="side-tab"></div>

    <h1 class="company-name">Kowhai Advisory</h1>

    <ul class="contact-block">
      <li>P.O Box 40817</li>
      <li>Nelson 7010 New Zealand</li>
      <li>
        <svg class="contact-icon" viewBox="0 0 12 12" aria-hidden="true">
          <path class="solid" d="M2.2 1 L4.4 1 L5 3.6 L3.7 4.6 C4.4 6.2 5.8 7.6 7.4 8.3 L8.4 7 L11 7.6 L11 9.8 C11 10.5 10.4 11 9.7 11 C5 10.6 1.4 7 1 2.3 C1 1.6 1.5 1 2.2 1 Z"/>
        </svg>
        + 64 21 555 0142
      </li>
      <li>
        <svg class="contact-icon" viewBox="0 0 12 12" aria-hidden="true">
          <rect x="1" y="2.5" width="10" height="7"/>
          <path d="M1 2.5 L6 6.5 L11 2.5"/>
        </svg>
        hello@kowhaiadvisory.co.nz
      </li>
      <li>
        <svg class="contact-icon" viewBox="0 0 12 12" aria-hidden="true">
          <circle cx="6" cy="6" r="5"/>
          <path d="M1 6 H11 M6 1 C3.5 3.5 3.5 8.5 6 11 M6 1 C8.5 3.5 8.5 8.5 6 11"/>
        </svg>
        www.kowhaiadvisory.co.nz
      </li>
    </ul>
  </main>
</body>
</html>
```